Brindle construction ltd staionary design
Project: Stationary
Stationary - Construction
Stationary
Professional
Directors Dan Brindle / Mark Brindle
BRINDLE CONSTRUCTION (GLOUCESTER) LTD
14 wexcombe road Gloucester GL4 8RQ
Brindleconstructionltd@fernmail.example
www.brindleconstructionlimited.example
would like stationary pack designed: business card, letterhead, envelope ect. Also a site sign please. Business card i would like black background to contrast my green logo with the logo in middle and details underneath. Letterhead i will leave to designer to come up with options. On site sign can i have logo ontop as main feature and underneath contact info with services incl ( New Builds, Extensions, Conversions, Refurbishments, Groundworks, Block Paving.) In logo attached use main logo ontop.
Main logo and underneath building contractor & Block paving specialist

```html
<!DOCTYPE html>
<html lang="en">
<head>
<meta charset="utf-8">
<title>Brindle Construction Ltd – Business Card</title>
<link rel="stylesheet" href="https://fonts.googleapis.com/css2?family=Exo+2:wght@300;400;800&display=swap">
<style>
  :root {
    --backdrop: #1c1c1c;
    --card-top: #1a1a1a;
    --card-bottom: #060606;
    --brand-green: #3fd22a;
    --band-green: #2fb41c;
    --band-dark: #0f5a08;
    --text-grey: #8a8a8a;
    --brand-grey: #5b5b5b;
  }
  * { margin: 0; padding: 0; box-sizing: border-box; }
  html, body { width: 1200px; height: 883px; overflow: hidden; }
  body {
    background: var(--backdrop);
    font-family: "Exo 2", Arial, sans-serif;
    position: relative;
  }
  .card {
    position: absolute;
    border-radius: 22px;
    background: linear-gradient(160deg, var(--card-top), var(--card-bottom));
    overflow: hidden;
    box-shadow: 0 6px 18px rgba(0,0,0,0.6);
  }
  .card--front { left: 161px; top: 91px; width: 528px; height: 365px; }
  .card--back  { left: 432px; top: 470px; width: 540px; height: 368px; }

  .brand {
    position: absolute;
    left: 0; right: 0;
    text-align: center;
    font-weight: 800;
    text-transform: uppercase;
    line-height: 1;
  }
  .card--front .brand { top: 38px; color: var(--brand-green); }
  .card--back .brand  { top: 132px; color: var(--brand-grey); }
  .brand__name { display: block; font-size: 50px; letter-spacing: 3px; }
  .brand__suffix { display: block; font-size: 17px; letter-spacing: 4px; margin-top: 6px; }

  .details {
    position: absolute;
    top: 152px; left: 0; right: 0;
    text-align: center;
    text-transform: uppercase;
    font-weight: 300;
    color: var(--text-grey);
    font-size: 11px;
    letter-spacing: 1px;
  }
  .details__directors { color: var(--brand-green); font-size: 15px; font-weight: 400; }
  .details__company { margin-top: 6px; font-size: 9px; }
  .details__contact { list-style: none; margin-top: 36px; }
  .details__contact li { line-height: 24px; }

  .band {
    position: absolute;
    left: 0; right: 0; bottom: 6px; height: 18px;
    background: linear-gradient(180deg, var(--band-green), var(--band-dark));
  }
</style>
</head>
<body>
  <section class="card card--front" aria-label="Business card front">
    <div class="brand">
      <span class="brand__name">Brindle</span>
      <span class="brand__suffix">Construction Ltd</span>
    </div>
    <div class="details">
      <p class="details__directors">Directors Dan Brindle / Mark Brindle</p>
      <p class="details__company">Brindle Construction (Gloucester) Ltd</p>
      <ul class="details__contact">
        <li>14 Wexcombe Road, Gloucester, GL4 8RQ</li>
        <li>P : 01632 960418</li>
        <li>C : 07700 900412 / 07700 900587</li>
        <li>E : brindleconstructionltd@fernmail.example</li>
        <li>W : www.brindleconstructionlimited.example</li>
      </ul>
    </div>
    <div class="band"></div>
  </section>

  <section class="card card--back" aria-label="Business card back">
    <div class="brand">
      <span class="brand__name">Brindle</span>
      <span class="brand__suffix">Construction Ltd</span>
    </div>
  </section>
</body>
</html>
```